Corvena Card

The logo is the Spanish flag colors I want a vibrant eye catching design with the yellow / red colors over either Navy or white background or black even ,
Would like a 2D feel to the logo with another lighter color logo under it look ,

Contact Information for Business Card

Corvena Flooring
Tobin Reswick
Main Number
Cell Number
Fax Number

Website on the side of the card somewhere

Font styles to use
Sans Serif

Colors
ec1f27
ffc214

Requirements
Must have
• 2 logos feel one is bolder and the other one underneath very light

```html
<!DOCTYPE html>
<html lang="en">
<head>
<meta charset="utf-8">
<title>Corvena Flooring – Business Card</title>
<link href="https://fonts.googleapis.com/css2?family=Exo+2:wght@400;500;600&display=swap" rel="stylesheet">
<style>
  :root {
    --backdrop: #e4e4e4;
    --card: #333333;
    --red: #ec1f27;
    --red-print: #b8302d;
    --yellow: #ffc214;
    --yellow-print: #e9bd44;
    --ink-light: #c9c9c9;
  }
  * { margin: 0; padding: 0; box-sizing: border-box; }
  html, body {
    width: 1200px;
    height: 790px;
    overflow: hidden;
    background: var(--backdrop);
    font-family: "Exo 2", Arial, sans-serif;
  }
  .canvas {
    position: relative;
    width: 1200px;
    height: 790px;
  }
  .card {
    position: absolute;
    top: 232px;
    width: 480px;
    height: 274px;
    background: var(--card);
    overflow: hidden;
  }
  .card--front { left: 103px; }
  .card--back { left: 611px; }

  .brand-band {
    position: absolute;
    top: 0;
    width: 136px;
    height: 274px;
  }
  .card--front .brand-band {
    right: 0;
    background: linear-gradient(135deg, var(--red-print) 0%, #c9562f 50%, var(--yellow-print) 100%);
  }
  .card--back .brand-band {
    left: 0;
    background: linear-gradient(225deg, var(--red-print) 0%, #c9562f 50%, var(--yellow-print) 100%);
  }

  .person {
    position: absolute;
    left: 73px;
    top: 79px;
  }
  .person__name {
    font-size: 16px;
    font-weight: 600;
    color: var(--red-print);
    letter-spacing: 0.2px;
    line-height: 1;
  }
  .person__role {
    margin-top: 5px;
    font-size: 11px;
    font-weight: 500;
    color: var(--yellow-print);
    line-height: 1;
  }
  .contact {
    position: absolute;
    left: 73px;
    top: 130px;
    list-style: none;
  }
  .contact__item {
    display: flex;
    align-items: center;
    height: 13.6px;
    font-size: 11.5px;
    color: var(--ink-light);
    line-height: 1;
  }
  .contact__icon {
    width: 9px;
    height: 9px;
    margin-right: 7px;
    fill: var(--yellow-print);
    flex: none;
  }

  .brand {
    position: absolute;
    left: 301px;
    top: 172px;
    transform: translateX(-50%);
    display: flex;
    align-items: center;
    gap: 8px;
    white-space: nowrap;
  }
  .brand__mark {
    width: 12px;
    height: 12px;
    background: var(--red-print);
    flex: none;
  }
  .brand__name {
    font-size: 16px;
    font-weight: 600;
    letter-spacing: 3px;
    text-transform: uppercase;
    color: var(--yellow-print);
    line-height: 1;
  }
</style>
</head>
<body>
<main class="canvas">

  <section class="card card--front" aria-label="Card front">
    <div class="brand-band" role="img" aria-label="Brand pattern in red and yellow"></div>
    <div class="person">
      <p class="person__name">TOBIN RESWICK</p>
      <p class="person__role">President</p>
    </div>
    <ul class="contact">
      <li class="contact__item">
        <svg class="contact__icon" viewBox="0 0 10 10" aria-hidden="true"><path d="M2 0.5 3.6 2.6 2.7 3.6C3.3 5 4.7 6.4 6.3 7.2L7.3 6.3 9.5 7.9 8.6 9.5C4.5 9.2 0.8 5.4 0.5 1.4Z"/></svg>
        <span>555-214-7730</span>
      </li>
      <li class="contact__item">
        <svg class="contact__icon" viewBox="0 0 10 10" aria-hidden="true"><path d="M2.5 0h5a1 1 0 0 1 1 1v8a1 1 0 0 1-1 1h-5a1 1 0 0 1-1-1V1a1 1 0 0 1 1-1Zm.3 1.2v6.6h4.4V1.2Z"/></svg>
        <span>555-518-2046</span>
      </li>
      <li class="contact__item">
        <svg class="contact__icon" viewBox="0 0 10 10" aria-hidden="true"><path d="M2.5 0h5v3h-5ZM0.5 3.5h9v4.5h-9ZM2 8.5h6V10H2Z"/></svg>
        <span>555-327-9184</span>
      </li>
      <li class="contact__item">
        <svg class="contact__icon" viewBox="0 0 10 10" aria-hidden="true"><path d="M0.5 2h9v6h-9Zm0.9 0.8L5 5.5l3.6-2.7Z" fill-rule="evenodd"/></svg>
        <span>info@corvena.com</span>
      </li>
      <li class="contact__item">
        <svg class="contact__icon" viewBox="0 0 10 10" aria-hidden="true"><circle cx="5" cy="5" r="4.6"/></svg>
        <span>www.corvena.com</span>
      </li>
    </ul>
  </section>

  <section class="card card--back" aria-label="Card back">
    <div class="brand-band" role="img" aria-label="Brand pattern in red and yellow"></div>
    <div class="brand">
      <span class="brand__mark" aria-hidden="true"></span>
      <p class="brand__name">Corvena Flooring</p>
    </div>
  </section>

</main>
</body>
</html>
```